HUSH: Halt Usual Stuff Happily school library event

I need two poster designs for Halt Usual Stuff Happily (HUSH) in BC, requested by the CSMKA--Cedarvale School Media Keepers' Association. One should be for elementary students and one for high school. I want the date (Monday, October 26, 2020) and Halt Usual Stuff Happily. I would like the posters in English and in French. French is : Mets Ta Journée En Pause! I'm including last year's posters as examples. I would like to be able to print the poster files on 11x17 paper.

Requirements
Must have
• -The phrase "Halt Usual Stuff Happily" for the English version; "Mets Ta Journée En Pause" for the French version.
-Include the organization name: Cedarvale School Media Keepers' Association
-The date: Monday, October 26, 2020
Nice to have
• I would like the elementary version to be bright and colourful--fun for younger kids. I would like the high school version to be a bit more mature for the older students. Can still be bright and colourful.

```html
<!DOCTYPE html>
<html lang="en">
<head>
<meta charset="utf-8">
<title>HUSH – Halt Usual Stuff Happily posters</title>
<link rel="stylesheet" href="https://fonts.googleapis.com/css2?family=Anton&family=Gochi+Hand&family=Josefin+Sans:wght@300;400&family=Playfair+Display:ital,wght@0,700;1,400&family=Righteous&family=Special+Elite&family=Titan+One&display=swap">
<style>
  :root {
    --sky: #27aae1;
    --ink: #231f20;
    --paper: #ffffff;
    --tag-green: #7ac143;
    --berry-red: #c1202f;
    --sun-orange: #f7941d;
    --grape: #7b3f98;
    --lemon: #f2d31b;
  }
  * { margin: 0; padding: 0; box-sizing: border-box; }
  html, body {
    width: 1200px; height: 612px; overflow: hidden;
    background: var(--paper);
  }
  .poster-set { position: relative; width: 1200px; height: 612px; }

  .poster {
    position: absolute; top: 96px;
    width: 276px; height: 426px;
    background: var(--sky);
    overflow: hidden;
  }
  .poster--en-senior { left: 19px; }
  .poster--en-junior { left: 310px; top: 97px; }
  .poster--fr-senior { left: 623px; }
  .poster--fr-junior { left: 914px; top: 97px; }

  .org-name {
    position: absolute; top: 16px; left: 0; width: 100%;
    text-align: center;
    font-family: "Josefin Sans", sans-serif; font-weight: 400;
    font-size: 10.5px; line-height: 15px; letter-spacing: 0.2px;
    color: var(--ink); text-transform: uppercase;
  }

  .frame {
    position: absolute; left: 33px; top: 91px;
    width: 210px; height: 310px;
    border: 1px solid var(--paper);
  }

  .date-tag {
    position: absolute; left: 17px; top: 80px;
    width: 146px; height: 28px;
    background: var(--tag-green);
    transform: rotate(-10deg);
    font-family: "Special Elite", monospace;
    font-size: 13px; line-height: 28px;
    text-align: center; color: var(--ink);
    z-index: 2;
  }

  .word {
    position: absolute; left: 0; width: 100%;
    text-align: center; white-space: nowrap;
    z-index: 3;
  }

  /* Senior (mature) style */
  .senior .word { color: var(--paper); text-shadow: 2px 2px 0 var(--ink); }
  .word--serif-bold { font-family: "Playfair Display", serif; font-weight: 700; }
  .word--serif-italic { font-family: "Playfair Display", serif; font-style: italic; font-weight: 400; }
  .word--thin { font-family: "Josefin Sans", sans-serif; font-weight: 300; }
  .word--heavy { font-family: "Anton", sans-serif; text-transform: uppercase; }

  /* Junior (playful) style */
  .junior .word { text-shadow: 2px 2px 0 var(--ink); }
  .word--chunky { font-family: "Titan One", sans-serif; color: var(--berry-red); text-transform: uppercase; }
  .word--hand { font-family: "Gochi Hand", cursive; color: var(--sun-orange); }
  .word--round { font-family: "Righteous", sans-serif; color: var(--grape); }

  .lettering-art {
    position: absolute; z-index: 3;
    border-radius: 6px;
    background: linear-gradient(135deg, rgba(242,211,27,0.85), rgba(242,211,27,0.55));
  }

  /* English senior */
  .poster--en-senior .w1 { top: 96px; font-size: 62px; line-height: 70px; }
  .poster--en-senior .w2 { top: 160px; font-size: 38px; line-height: 46px; }
  .poster--en-senior .w3 { top: 218px; font-size: 72px; line-height: 80px; }
  .poster--en-senior .w4 { top: 322px; font-size: 48px; line-height: 60px; transform: scaleY(1.35); }

  /* English junior */
  .poster--en-junior .w1 { top: 108px; font-size: 46px; line-height: 56px; }
  .poster--en-junior .w2 { top: 168px; font-size: 48px; line-height: 56px; }
  .poster--en-junior .art { left: 53px; top: 241px; width: 164px; height: 65px; }
  .poster--en-junior .w4 { top: 318px; font-size: 50px; line-height: 60px; }

  /* French senior */
  .poster--fr-senior .w1 { top: 100px; font-size: 54px; line-height: 62px; }
  .poster--fr-senior .w2 { top: 140px; font-size: 92px; line-height: 100px; }
  .poster--fr-senior .w3 { top: 228px; font-size: 32px; line-height: 40px; }
  .poster--fr-senior .w4 { top: 290px; font-size: 62px; line-height: 80px; transform: scaleY(1.5); }

  /* French junior */
  .poster--fr-junior .w1 { top: 104px; font-size: 46px; line-height: 56px; }
  .poster--fr-junior .w2 { top: 152px; font-size: 40px; line-height: 46px; }
  .poster--fr-junior .art { left: 59px; top: 196px; width: 154px; height: 70px; }
  .poster--fr-junior .w4 { top: 286px; font-size: 66px; line-height: 80px; }
</style>
</head>
<body>
<main class="poster-set">

  <section class="poster senior poster--en-senior" aria-label="High school poster, English">
    <p class="org-name">Cedarvale School<br>Media Keepers’ Association</p>
    <div class="frame"></div>
    <p class="date-tag">MONDAY, 26/10/2020</p>
    <h1 class="word word--serif-bold w1">Halt</h1>
    <p class="word word--serif-italic w2">usual</p>
    <p class="word word--thin w3">stuff</p>
    <p class="word word--heavy w4">Happily</p>
  </section>

  <section class="poster junior poster--en-junior" aria-label="Elementary poster, English">
    <p class="org-name">Cedarvale School<br>Media Keepers’ Association</p>
    <div class="frame"></div>
    <p class="date-tag">MONDAY, 26/10/2020</p>
    <h1 class="word word--chunky w1">Halt</h1>
    <p class="word word--hand w2">usual</p>
    <div class="lettering-art art" role="img" aria-label="Hand-drawn yellow animal lettering spelling the word STUFF"></div>
    <p class="word word--round w4">happily</p>
  </section>

  <section class="poster senior poster--fr-senior" aria-label="Affiche secondaire, français" lang="fr">
    <p class="org-name">Cedarvale School<br>Media Keepers’ Association</p>
    <div class="frame"></div>
    <p class="date-tag">LUNDI, 26/10/2020</p>
    <h1 class="word word--serif-bold w1">Mets</h1>
    <p class="word word--serif-italic w2">ta</p>
    <p class="word word--thin w3">journée en</p>
    <p class="word word--heavy w4">Pause</p>
  </section>

  <section class="poster junior poster--fr-junior" aria-label="Affiche primaire, français" lang="fr">
    <p class="org-name">Cedarvale School<br>Media Keepers’ Association</p>
    <div class="frame"></div>
    <p class="date-tag">LUNDI, 26/10/2020</p>
    <h1 class="word word--chunky w1">Mets</h1>
    <p class="word word--hand w2">ta journée</p>
    <div class="lettering-art art" role="img" aria-label="Lettrage jaune dessiné à la main formant le mot EN"></div>
    <p class="word word--round w4">Pause</p>
  </section>

</main>
</body>
</html>
```